HiItsJonBrell.com needs a modern, eye-catching business card design

My name is Jon Brell and I own a video training (software development industry) website. I need a business card design that is eye catching for when I travel to conferences or do seminars. I would prefer something simple but bold. Something along the lines of this: https://pixvaultstatic.example/gallery_img/530172/44018/44018_9917302_530172_image.jpg

Note that I do not have a specific logo, but I do have an caricature I use on my site of myself. I've not attached it because I'm not really a fan of having it on my business cards. I would prefer lettering instead of an image. You can go to my website (https://hiitsjonbrell.com) for inspiration.

I want to add the following information on my card (the order of these, their size, and their casing is up to you):

Jon Brell
jon@HiItsJonBrell.com
@HiItsJonBrell
HiItsJonBrell.com
vidsharehub.example/HiItsJonBrell

I would also like to have somewhere on the card a small ad that says "Get a free course at https://HiItsJonBrell.com/FreeCourse". Feel free to play with that wording or layout if you need. I would prefer this text to be at the bottom of the card and subtle. Some small eye-catching thing might be ok but nothing huge or garish.

I plan on printing this card at pressquill.example (https://www.pressquill.example/us/design-guidelines/business-cards.html). I would like it to be the standard size (3.66" x 2.16"). I would prefer rounded corners and horizontal orientation. This is a two-side design. I would prefer the side with all of the information be primarily white but I like color text (again, flexible on that). On the front side, I like simple. Maybe just HiItsJonBrell.com (casing on that is up to you - whatever looks and reads the best - that goes for all of the casing). As for font choices, I prefer a modern, clean font. For example, Open Sans Light can be a nice option.

Website Info (might be helpful for the card):
Color Palette

Darkest blue - #263246
Alternate blue - #2F4E6A
Light blue - #2A98C3
Orange - #FF6201
White - #FFFFFF

Font for Jon Brell Logo

Jellyka Estryas Handwriting
http://www.typecrate.example/jellyka_estryas_handwriting.font

Fonts for Site Content and VidShare Thumbnails

Lovelo (bold title font)
http://www.glyphmill.example/lovelo-font/

Open Sans (body font)
http://www.letterbarn.example/fonts/open-sans

Industry/Entity Type

Software Development

Contact Information for Business Card

Jon Brell
jon@HiItsJonBrell.com
@HiItsJonBrell
HiItsJonBrell.com
vidsharehub.example/HiItsJonBrell

Get a free course at https://HiItsJonBrell.com/FreeCourse

Colors

Designer to choose colors to be used in the design.

Requirements
Nice to have
• Modern color - maybe primarily a color on the front and then that color as an accent on the back.
Should not have
• Lots of colors - I LOVE color but do not want a rainbow of colors on the card.

```html
<!DOCTYPE html>
<html lang="en">
<head>
<meta charset="utf-8">
<title>Jon Brell – Business Card</title>
<link rel="stylesheet" href="https://fonts.googleapis.com/css2?family=Open+Sans:wght@400;700&display=swap">
<style>
  :root {
    --paper: #ffffff;
    --ink-dark: #222222;
    --ink-mid: #555555;
    --ink-soft: #333333;
    --accent: #1d5c8a;
    --accent-icon: #1a6596;
    --rule-grey: #d6d6d6;
    --lettering-a: #e3eef6;
    --lettering-b: #c9deee;
  }
  * { margin: 0; padding: 0; box-sizing: border-box; }
  html, body { width: 1200px; height: 720px; overflow: hidden; background: var(--paper); }
  body { font-family: "Open Sans", Arial, sans-serif; position: relative; }

  .card { position: relative; width: 1200px; height: 720px; background: var(--paper); }

  .identity { position: absolute; right: 95px; top: 68px; text-align: right; }
  .identity__name { font-weight: 700; font-size: 45px; color: var(--ink-dark); letter-spacing: 0.5px; line-height: 1.1; }
  .identity__role { font-size: 26px; color: var(--ink-mid); margin-top: 4px; line-height: 1.2; }
  .identity__rule { position: absolute; right: 0; top: 107px; width: 63px; height: 5px; background: var(--rule-grey); }

  .signature {
    position: absolute; left: 121px; top: 286px; width: 336px; height: 134px;
    background: linear-gradient(135deg, var(--lettering-a), var(--lettering-b));
    border-radius: 6px;
  }

  .divider { position: absolute; left: 545px; top: 224px; width: 3px; height: 319px; background: var(--accent); }

  .contacts { position: absolute; left: 635px; top: 226px; list-style: none; }
  .contacts__item { display: grid; grid-template-columns: 80px auto; align-items: center; column-gap: 10px; height: 52px; margin-bottom: 6px; }
  .contacts__item:nth-child(4), .contacts__item:nth-child(5) { margin-top: 2px; }
  .contacts__icon { display: flex; justify-content: center; align-items: center; }
  .contacts__label { font-size: 13px; font-weight: 700; color: var(--accent-icon); }
  .contacts__text { font-size: 25px; color: var(--ink-mid); }

  .promo { position: absolute; left: 840px; top: 570px; transform: translateX(-50%); text-align: center; font-size: 21px; line-height: 30px; color: var(--ink-soft); white-space: nowrap; }
</style>
</head>
<body>
  <main class="card">
    <header class="identity">
      <h1 class="identity__name">Jon Brell</h1>
      <p class="identity__role">Software Developer</p>
      <div class="identity__rule"></div>
    </header>

    <div class="signature" role="img" aria-label="Handwritten signature lettering of Jon Brell in blue ink"></div>

    <div class="divider"></div>

    <ul class="contacts">
      <li class="contacts__item">
        <span class="contacts__icon">
          <svg width="32" height="30" viewBox="0 0 32 30" aria-hidden="true">
            <rect x="7" y="1" width="18" height="14" fill="var(--accent-icon)"/>
            <rect x="10" y="4" width="12" height="2" fill="#fff"/>
            <rect x="10" y="8" width="12" height="2" fill="#fff"/>
            <path d="M2 12 L16 22 L30 12 V29 H2 Z" fill="var(--accent-icon)"/>
            <path d="M2 29 L13 20 M30 29 L19 20" stroke="#fff" stroke-width="1.5"/>
          </svg>
        </span>
        <span class="contacts__text">jon@HiItsJonBrell.com</span>
      </li>
      <li class="contacts__item">
        <span class="contacts__icon">
          <svg width="34" height="34" viewBox="0 0 34 34" aria-hidden="true">
            <g fill="none" stroke="var(--accent-icon)" stroke-width="2.5">
              <circle cx="15" cy="15" r="12"/>
              <ellipse cx="15" cy="15" rx="5" ry="12"/>
              <line x1="3" y1="15" x2="27" y2="15"/>
              <line x1="5" y1="9" x2="25" y2="9"/>
              <line x1="5" y1="21" x2="25" y2="21"/>
            </g>
            <path d="M20 18 L32 26 L27 27 L30 33 L28 34 L25 28 L21 31 Z" fill="var(--accent-icon)" stroke="#fff" stroke-width="1"/>
          </svg>
        </span>
        <span class="contacts__text">HiItsJonBrell.com</span>
      </li>
      <li class="contacts__item">
        <span class="contacts__icon contacts__label">Chirper</span>
        <span class="contacts__text">@HiItsJonBrell</span>
      </li>
      <li class="contacts__item">
        <span class="contacts__icon contacts__label">FriendBook</span>
        <span class="contacts__text">@HiItsJonBrell</span>
      </li>
      <li class="contacts__item">
        <span class="contacts__icon contacts__label">VidShare</span>
        <span class="contacts__text">@HiItsJonBrell</span>
      </li>
    </ul>

    <p class="promo">Get a free course at<br>https://HiItsJonBrell.com/FreeCourse</p>
  </main>
</body>
</html>
```